Refreshed PPT Presentation for US based firms

There are basically 4 types of slides in this presentation:
* Roadmap (Title, Agenda, Billboards)
* Teaching (Content, Examples)
* Samples (Real life samples)
* Polls (Placeholders for interactive polls)
We want new templates for each of these types of templates with coordinated graphics, images, icons and fonts.

```html
<!DOCTYPE html>
<html lang="en">
<head>
<meta charset="utf-8">
<title>Advice and Counsel Through Email</title>
<link href="https://fonts.googleapis.com/css2?family=Montserrat:wght@400;500;600;700;800&family=Tinos&family=Arimo&display=swap" rel="stylesheet">
<style>
:root{
  --stage:#666666;
  --slide:#f4f4f4;
  --slide-edge:#ececec;
  --ink:#111111;
  --muted:#444444;
  --pink:#e0248f;
  --pink-soft:#f7dce9;
  --frame:#5d7a8a;
  --dark:#1a1a1a;
}
*{box-sizing:border-box;margin:0;padding:0}
html,body{width:1200px;height:4079px;overflow:hidden}
body{background:var(--stage);position:relative;font-family:"Montserrat",sans-serif;color:var(--ink)}
.slide{position:absolute;left:38px;width:1121px;height:630px;overflow:hidden;
  background:linear-gradient(135deg,#f8f8f8 0%,var(--slide) 50%,var(--slide-edge) 100%)}
.s1{top:43px}.s2{top:714px}.s3{top:1387px}.s4{top:2058px}.s5{top:2729px}.s6{top:3400px}
.abs{position:absolute}
.tag{position:absolute;right:19px;top:38px;font-weight:700;font-size:20px;letter-spacing:.3px}
.slide-title{position:absolute;font-weight:700;font-size:30px;letter-spacing:.3px}
.photo{position:absolute;border-radius:50%}

/* title slide */
.s1 .tag{left:62px;right:auto;top:44px;font-size:19px}
.hero-title{left:57px;top:132px;font-weight:800;font-size:58px;line-height:73px;letter-spacing:1px}
.presenter{left:60px;top:450px;font-weight:700;font-size:19px}
.poll-link{left:60px;top:491px;font-weight:700;font-size:15px;color:var(--pink)}
.hero-photo{left:560px;top:45px;width:473px;height:473px;background:radial-gradient(circle at 45% 45%,#e9e4df,#c9c3bd 60%,#8f8a86)}

/* chart slide */
.chart{position:absolute;left:0;top:0;width:1121px;height:630px;font-family:"Montserrat",sans-serif}
.stat{position:absolute;left:632px;width:416px;height:105px;background:#fff;border-left:5px solid var(--pink);
  border-radius:10px;box-shadow:0 4px 14px rgba(0,0,0,.07);padding:0 24px;display:flex;align-items:center;
  font-weight:700;font-size:17px;line-height:27px}

/* sample email slide */
.memo{position:absolute;left:415px;top:51px;width:402px;border-collapse:collapse;font-family:"Arimo",sans-serif;font-size:11px;line-height:13px;background:#fff}
.memo td{border:1px solid #222;padding:2px 4px;vertical-align:top}
.memo td:first-child{width:63px}
.letter{position:absolute;left:416px;width:664px;font-family:"Tinos",serif;font-size:12px;line-height:27px;color:#222}

/* agenda */
.agenda-title{left:57px;top:65px;font-weight:700;font-size:38px}
.agenda-item{position:absolute;left:62px;font-weight:700;font-size:19px;display:flex;align-items:center;gap:10px}
.agenda-item.sub{left:96px;font-size:15px;gap:8px}
.dot{width:12px;height:12px;border-radius:50%;border:3px solid var(--pink);flex:none}
.sub .dot{width:10px;height:10px;border-width:2.5px}
.sky-photo{left:603px;top:135px;width:680px;height:680px;background:radial-gradient(circle at 55% 45%,#b7cde0,#9fbad3)}

/* writing process */
.process-title{left:46px;top:40px;font-weight:700;font-size:31px}
.stage{position:absolute;left:66px;width:385px;font-size:17px;line-height:32px;color:#333;padding-left:20px}
.stage::before{content:"";position:absolute;left:0;top:10px;width:10px;height:10px;border-radius:50%;border:2.5px solid var(--pink);box-sizing:border-box}
.halo{left:532px;top:97px;width:490px;height:490px;border-radius:50%;background:var(--pink-soft)}
.tile{position:absolute;border:4px solid var(--frame)}

/* interrupters */
.interrupt-title{left:0;right:0;top:240px;text-align:center;font-weight:700;font-size:34px}
.interrupt-text{left:176px;width:768px;top:310px;text-align:center;font-size:13px;line-height:26px;color:#333}
</style>
</head>
<body>

<section class="slide s1">
  <div class="tag">ADVICE AND COUNSEL</div>
  <h1 class="abs hero-title">ADVICE AND<br>COUNSEL<br>THROUGH<br>EMAIL</h1>
  <div class="abs presenter">DANA WHITMORE FOR NORTHGATE LEGAL P.C</div>
  <div class="abs poll-link">GO TO WWW.POLLSPACE.EXAMPLE/DANAWHITMORE21</div>
  <div class="photo hero-photo" role="img" aria-label="Photo of smiling colleagues applauding in an office"></div>
</section>

<section class="slide s2">
  <h2 class="slide-title" style="left:52px;top:32px">EMAIL OVERLOAD: WHY!Data Charts</h2>
  <div class="tag">ADVICE AND COUNSEL</div>
  <svg class="chart" viewBox="0 0 708 398" aria-label="Bar chart of emails per year 2017 to 2021">
    <g fill="#222" font-size="5.8" font-weight="600" text-anchor="end">
      <text x="51" y="122">700</text><text x="51" y="150">600</text><text x="51" y="179">500</text>
      <text x="51" y="206">400</text><text x="51" y="232">300</text><text x="51" y="259">200</text>
      <text x="51" y="286">100</text><text x="51" y="312">50</text><text x="51" y="339">0</text>
    </g>
    <line x1="56" y1="118" x2="56" y2="337" stroke="#999" stroke-width=".6"/>
    <line x1="56" y1="337" x2="361" y2="337" stroke="#999" stroke-width=".6"/>
    <g fill="#e0248f">
      <rect x="86" y="156" width="35" height="181"/>
      <rect x="143" y="172" width="35" height="165"/>
      <rect x="199" y="186" width="35" height="151"/>
      <rect x="256" y="212" width="35" height="125"/>
      <rect x="306" y="226" width="34" height="111"/>
    </g>
    <g fill="#222" font-size="5.8" font-weight="600" text-anchor="middle">
      <text x="103" y="358">2017</text><text x="160" y="358">2018</text><text x="216" y="358">2019</text>
      <text x="273" y="358">2020</text><text x="323" y="358">2021</text>
    </g>
  </svg>
  <div class="stat" style="top:125px">According to Halvern Research, in 2022 333.2 billion emails were sent per day</div>
  <div class="stat" style="top:247px">In 2018, the number of emails received per day by average worker: 121</div>
  <div class="stat" style="top:369px">Tremendous improvement over communications in mid-1990s</div>
  <div class="stat" style="top:491px">Tremendous improvement over communications in mid-1990s</div>
</section>

<section class="slide s3">
  <svg class="abs" style="left:0;top:0" width="1121" height="630" role="img" aria-label="Photo of two colleagues working at a laptop">
    <defs><linearGradient id="office" x1="0" y1="0" x2="1" y2="1"><stop offset="0" stop-color="#6f8690"/><stop offset=".6" stop-color="#4c5658"/><stop offset="1" stop-color="#c9cdd0"/></linearGradient></defs>
    <circle cx="12" cy="314" r="390" fill="url(#office)"/>
  </svg>
  <div class="tag">ADVICE AND COUNSEL</div>
  <table class="memo">
    <tr><td>To</td><td>Ledgerline on Call</td></tr>
    <tr><td>From</td><td>Ray Colbert<br>Associate Counsel, Employment Law<br>KL Holdings</td></tr>
    <tr><td>Subject</td><td>Medical Marijuana</td></tr>
  </table>
  <p class="letter" style="top:193px">Our HR VP wants us to eliminate the company’s practice of allowing employees to use marijuana at home or at work upon the employee’s attestation of a medical need for medical marijuana. Some executives have complained to HR that marijuana use at work is degrading productivity and damaging our reputation with clients and potential clients.</p>
  <p class="letter" style="top:300px">By the way, I don’t allow any employees in the corporate compliance department to use marijuana under any circumstances, no matter where the employee is located. We randomly test them and fire anyone who fails the test.</p>
  <p class="letter" style="top:381px">We want to be as restrictive as possible and make a complete 360-degree change, while complying with applicable federal and state laws. Please answer a narrow question with these facts in mind. Can we maintain a marijuana-free company? If not, what’s the most we can do to duplicate my department’s practice throughout the rest of the company?</p>
  <p class="letter" style="top:516px">I have a meeting next week with the HR VP who wants to move in this direction, and I’d like to have an answer then. Can you get back to me by tomorrow?</p>
</section>

<section class="slide s4">
  <div class="tag">ADVICE AND COUNSEL</div>
  <h2 class="abs agenda-title">AGENDA</h2>
  <div class="agenda-item" style="top:157px"><span class="dot"></span>PREPARATION AND PROCESS</div>
  <div class="agenda-item" style="top:210px"><span class="dot"></span>AUDIENCE AND PURPOSE</div>
  <div class="agenda-item" style="top:262px"><span class="dot"></span>CHARACTERISTICS OF A QUALITY RESPONSE</div>
  <div class="agenda-item sub" style="top:316px"><span class="dot"></span>QUICK</div>
  <div class="agenda-item sub" style="top:363px"><span class="dot"></span>CLEAR</div>
  <div class="agenda-item sub" style="top:409px"><span class="dot"></span>CONCISE</div>
  <div class="photo sky-photo" role="img" aria-label="Photo of skydivers forming a ring formation against the sky"></div>
</section>

<section class="slide s5">
  <div class="tag">ADVICE AND COUNSEL</div>
  <h2 class="abs process-title">FOUR STAGES OF THE WRITING PROCESS</h2>
  <p class="stage" style="top:141px">Madman, the creative force who generates the ideas</p>
  <p class="stage" style="top:234px">Architect, the planner who builds the structure for the document</p>
  <p class="stage" style="top:328px">Carpenter, the craftsman who writes a draft</p>
  <p class="stage" style="top:421px">Judge, the reviewer who edits the draft</p>
  <div class="abs halo"></div>
  <div class="tile" style="left:510px;top:152px;width:263px;height:169px;background:#fafafa" role="img" aria-label="Illustration of a head silhouette surrounded by thought bubbles"></div>
  <div class="tile" style="left:793px;top:152px;width:258px;height:169px;background:linear-gradient(135deg,#f6d3e3,#ecb5cd)" role="img" aria-label="Photo of a wooden judge's gavel"></div>
  <div class="tile" style="left:510px;top:348px;width:258px;height:169px;background:linear-gradient(135deg,#ffffff,#e9e3dd)" role="img" aria-label="Photo of a claw hammer"></div>
  <div class="tile" style="left:793px;top:348px;width:261px;height:169px;background:linear-gradient(135deg,#e6ebef,#c9b79a)" role="img" aria-label="Photo of a drafting board with set squares"></div>
</section>

<section class="slide s6">
  <svg class="abs" style="left:0;top:0" width="1121" height="630" viewBox="0 0 708 398">
    <ellipse cx="140" cy="-60" rx="210" ry="160" fill="#e0248f"/>
    <ellipse cx="680" cy="600" rx="380" ry="290" fill="#1a1a1a"/>
  </svg>
  <div class="tag">ADVICE AND COUNSEL</div>
  <h2 class="abs interrupt-title">SUBJECT - VERB – OBJECT INTERRUPTERS</h2>
  <p class="abs interrupt-text">In his letter on November 10, 2003 (“Exhibit A”), Mr. Brookfield with Brookfield Trading, LLC asked us to describe and evaluate the legal advice we have given to the Company. The request relates to your recent examination of the Company’s financial statements. (About 50% of the original)</p>
</section>

</body>
</html>
```